We need a flyer designed for our 4th Annual Brightfield: A Kinfolk Homecoming Harvest Festival that includes the day, time, location, address, and logos. It also needs to include what to expect. The event will be held on Saturday June 14th from 12p-6p at Lantern Commons located at 418 N. Corvella Ave., Pensacola, FL 32507. Please see uploaded files for prior flyers for reference when it comes to information to include. Also I've uploaded pictures from our prior festivals that you may incorporate and logos.

```html
<!DOCTYPE html>
<html lang="en">
<head>
<meta charset="utf-8">
<title>4th Annual Brightfield – A Kinfolk Homecoming Harvest Festival</title>
<link rel="stylesheet" href="https://fonts.googleapis.com/css2?family=Anton&family=Oswald:wght@700&family=Open+Sans:wght@700;800&display=swap">
<style>
  :root {
    --ink: #111111;
    --white: #ffffff;
    --sky: #2f97cf;
    --sun: #fff200;
    --tangerine: #f7941d;
    --crimson: #e4202f;
    --magenta: #e6197e;
    --leaf: #39b54a;
    --violet: #7b3fa0;
    --gold: #ffd21f;
    --shadow-grey: #8a8a8a;
  }
  * { box-sizing: border-box; margin: 0; padding: 0; }
  html, body { width: 927px; height: 1200px; overflow: hidden; background: var(--white); }
  .flyer {
    position: relative;
    width: 927px;
    height: 1200px;
    overflow: hidden;
    font-family: "Open Sans", Arial, sans-serif;
    background:
      radial-gradient(circle at 60% 55%, rgba(255,242,0,0.55) 0 18%, transparent 45%),
      conic-gradient(from 20deg at 55% 55%,
        var(--sun) 0deg 35deg, var(--tangerine) 35deg 70deg, var(--crimson) 70deg 100deg,
        var(--tangerine) 100deg 130deg, var(--sun) 130deg 160deg, var(--leaf) 160deg 190deg,
        var(--sky) 190deg 225deg, var(--violet) 225deg 255deg, var(--magenta) 255deg 290deg,
        var(--crimson) 290deg 320deg, var(--tangerine) 320deg 345deg, var(--sun) 345deg 360deg);
  }
  .tagline {
    position: absolute; top: 56px; left: 320px; width: 500px; text-align: center;
    font-family: "Oswald", Impact, sans-serif; font-weight: 700; font-size: 27px;
    letter-spacing: 0.5px; color: var(--ink);
  }
  .foundation {
    position: absolute; top: 106px; left: 230px; width: 560px; height: 76px;
    display: flex; align-items: center; gap: 16px;
  }
  .foundation-dot { width: 64px; height: 64px; border-radius: 50%; background: var(--white); flex: none; }
  .foundation-name { font-weight: 800; font-size: 30px; color: var(--ink); line-height: 1; }
  .presents {
    position: absolute; top: 182px; left: 320px; width: 500px; text-align: center;
    font-weight: 800; font-size: 25px; color: var(--ink);
  }
  .balloon-arch {
    position: absolute; top: 228px; left: 50px; width: 840px; height: 170px;
    border-radius: 420px 420px 40px 40px / 150px 150px 40px 40px;
    background: linear-gradient(90deg, #e4202f, #39b54a 25%, #ffd21f 45%, #e4202f 60%, #39b54a 80%, #ffd21f);
    opacity: 0.9;
  }
  .edition {
    position: absolute; top: 252px; left: 0; width: 927px; text-align: center;
    font-weight: 800; font-size: 38px; color: var(--ink);
  }
  .edition sup { font-size: 22px; }
  .title {
    position: absolute; top: 288px; left: 0; width: 927px; text-align: center;
    font-family: "Anton", Impact, sans-serif; font-size: 112px; line-height: 1;
    letter-spacing: 2px; color: #f4f4f4;
    text-shadow: 4px 5px 0 var(--shadow-grey), 6px 8px 6px rgba(0,0,0,0.35);
  }
  .subtitle {
    position: absolute; top: 418px; left: 0; width: 927px; text-align: center;
    font-weight: 800; font-size: 25px; color: var(--ink);
  }
  .features {
    position: absolute; top: 462px; left: 290px; width: 400px; text-align: center;
    font-weight: 800; font-size: 13.5px; line-height: 19px; color: var(--white);
    text-shadow: -1px -1px 0 var(--ink), 1px -1px 0 var(--ink), -1px 1px 0 var(--ink), 1px 1px 0 var(--ink);
  }
  .date-disc {
    position: absolute; left: 262px; top: 545px; width: 472px; height: 472px; border-radius: 50%;
    background: var(--sky); border: 5px solid rgba(255,255,255,0.85);
  }
  .day {
    position: absolute; top: 595px; left: 262px; width: 472px; text-align: center;
    font-weight: 800; font-size: 48px; color: var(--white); letter-spacing: 1px;
  }
  .date {
    position: absolute; top: 648px; left: 262px; width: 472px; text-align: center;
    font-family: "Anton", Impact, sans-serif; font-size: 92px; line-height: 1; color: var(--sun);
    text-shadow: 3px 4px 0 var(--ink);
  }
  .date sup { font-size: 50px; vertical-align: 38px; }
  .time {
    position: absolute; top: 749px; left: 348px; width: 318px; height: 50px; border-radius: 25px;
    background: var(--tangerine); border: 3px solid var(--ink);
    text-align: center; font-weight: 800; font-size: 36px; line-height: 43px; color: var(--ink);
  }
  .venue {
    position: absolute; top: 810px; left: 300px; width: 400px; text-align: center;
    font-weight: 700; font-size: 17px; color: var(--white); line-height: 1;
  }
  .venue .line { padding: 4px 0 9px; }
  .venue hr { border: 0; border-top: 2px solid var(--white); width: 280px; margin: 0 auto 9px; }
  .photo {
    position: absolute; border-radius: 50%; border: 4px solid var(--white);
  }
  .photo-hosts   { left: 65px;  top: 465px; width: 252px; height: 252px; background: linear-gradient(160deg, #7da45c, #e9e4dc 60%, #6b5a4a); }
  .photo-dancers { left: 669px; top: 483px; width: 168px; height: 168px; background: linear-gradient(180deg, #4a6a88, #3a3a3a 55%, #6f8e4c); }
  .photo-guests  { left: 716px; top: 649px; width: 190px; height: 190px; background: linear-gradient(160deg, #e5dfdc, #5d4638 60%, #d6d0cc); }
  .photo-crowd   { left: 76px;  top: 722px; width: 220px; height: 220px; background: linear-gradient(170deg, #9ab8c8, #d98a8a 45%, #7a5a4a); }
  .photo-steppers{ left: 698px; top: 875px; width: 204px; height: 204px; background: linear-gradient(180deg, #8fb06a, #6e4a8e 45%, #6d6a4a); }
  .photo-singers { left: 47px;  top: 939px; width: 158px; height: 158px; background: linear-gradient(170deg, #b9d3e6, #2f2f2f 60%, #3b88b8); }
  .photo-grill   { left: 218px; top: 897px; width: 224px; height: 224px; background: linear-gradient(180deg, #c7ccd2, #5e4a78 45%, #c6461e 85%); }
  .photo-stage   { left: 446px; top: 925px; width: 252px; height: 252px; background: linear-gradient(180deg, #f0efea, #c9a0a4 35%, #3a3a3a 60%, #8a9a6a); }
  .photo-drums   { left: 707px; top: 1065px; width: 112px; height: 112px; background: linear-gradient(180deg, #6a7a5a, #2d4a2d 55%, #8a5a3a); }
  .firm {
    position: absolute; left: 34px; top: 1128px; width: 236px; height: 53px;
    background: var(--ink); display: flex; align-items: center; gap: 10px; padding: 0 12px;
  }
  .firm-mark { width: 26px; height: 26px; background: var(--gold); flex: none; }
  .firm-name { font-weight: 700; font-size: 15px; color: var(--white); white-space: nowrap; }
</style>
</head>
<body>
<main class="flyer">
  <p class="tagline">CUMMUNITY | ARTS | CULTURE</p>

  <div class="foundation">
    <span class="foundation-dot"></span>
    <span class="foundation-name">The Harlow Family Foundation</span>
  </div>
  <p class="presents">PRESEANT</p>

  <div class="balloon-arch" role="img" aria-label="Red, black, yellow and green balloon arch behind the festival title"></div>
  <p class="edition">4<sup>th</sup> Annual</p>
  <h1 class="title">BRIGHTFIELD</h1>
  <p class="subtitle">A Kinfolk Homecoming Harvest Festival</p>

  <p class="features">
    LIVE PERFORMANCES | FOOD VENDORS |<br>
    ART/AFRICAN CLOTHING | KIDS OBSTACLE COURSE &amp;<br>
    PLAY AREA | SPADES &amp; DOMINO TABLES |<br>
    BRING YOUR OWN CHAIRS OR PICNIC BLANKETS
  </p>

  <div class="photo photo-hosts" role="img" aria-label="Festival hosts singing at a microphone in matching shirts"></div>
  <div class="photo photo-dancers" role="img" aria-label="Dance troupe performing on the lawn in front of a stage screen"></div>
  <div class="photo photo-guests" role="img" aria-label="Guests in sunglasses seated under the tents"></div>
  <div class="photo photo-crowd" role="img" aria-label="Families and children enjoying the festival crowd"></div>
  <div class="photo photo-steppers" role="img" aria-label="Youth step team performing in purple shirts"></div>
  <div class="photo photo-singers" role="img" aria-label="Performers singing together on stage"></div>

  <div class="date-disc"></div>
  <p class="day">SATURDAY</p>
  <p class="date">June 14<sup>th</sup></p>
  <p class="time">12pm-6pm</p>
  <div class="venue">
    <p class="line">at LANTERN COMMONS located at 418 N.</p>
    <hr>
    <p>Corvella Ave., Pensacola, FL 32507.</p>
  </div>

  <div class="photo photo-grill" role="img" aria-label="Food vendor grilling over an open flame"></div>
  <div class="photo photo-stage" role="img" aria-label="Attendees gathered in front of the festival stage"></div>
  <div class="photo photo-drums" role="img" aria-label="Drummers in traditional attire"></div>

  <div class="firm">
    <span class="firm-mark"></span>
    <span class="firm-name">The Harlow Firm, PLLC</span>
  </div>
</main>
</body>
</html>
```